RM Cargoline businesscard project

RM Cargoline Ltd is a freshly founded small (3 employees), young (average age is 30 years) company, living from the road transportation market without own tools.
We would like to have an impressive, new-line, cool busines card for a freshly founded forwarding company on an overcrowded market which raises attention and makes the potential partners eager to work with us.

Target Market(s)

The main profile of the company is logistic/forwarding on road.

Industry/Entity Type

Freight Forwarding

Contact Information for Business Card

Name: Berki Zsófia
Title: general manager
mobile nr: +36-70/482-5193
fax nr: +36-1/534-9061
e-mail: zsofia.berki@rmcargoline.example
info@rmcargoline.example
website address: http://www.rmcargoline.example
and if possible maybe some funny or helpful info on the back

Requirements
Must have
• contact details above
Nice to have
• some really nice and catching back-side (info, graphics, useful tool info... anything)
Should not have
• trucks, road, ship, airplane on it...

```html
<!DOCTYPE html>
<html lang="en">
<head>
<meta charset="utf-8">
<title>RM Cargoline – Business Card</title>
<link rel="stylesheet" href="https://fonts.googleapis.com/css2?family=Open+Sans:wght@400;600;700&display=swap">
<style>
  :root {
    --bg: #2b2b2d;
    --card-white: #ffffff;
    --blue: #5b8fd0;
    --blue-light: #86b4e2;
    --blue-dark: #4a7fc4;
    --ink: #333436;
    --ink-soft: #4a4a4a;
    --band-dark: #2a2a2c;
  }
  * { margin: 0; padding: 0; box-sizing: border-box; }
  html, body {
    width: 1200px; height: 900px; overflow: hidden;
    background: var(--bg);
    font-family: "Open Sans", Arial, sans-serif;
  }
  .canvas { position: relative; width: 1200px; height: 900px; }

  .card {
    position: absolute;
    width: 620px; height: 354px;
    border-radius: 3px;
    overflow: hidden;
    box-shadow: 0 14px 30px rgba(0,0,0,.45);
  }

  /* Back side */
  .card-back {
    left: 80px; top: 80px;
    background: linear-gradient(200deg, var(--blue) 0%, var(--blue-light) 60%, var(--blue) 100%);
  }
  .back-brand {
    position: absolute; left: 0; right: 0; top: 128px;
    display: flex; align-items: center; justify-content: center; gap: 14px;
    color: #fff; font-weight: 700; font-size: 48px; letter-spacing: -0.5px;
  }
  .back-brand .brand-square {
    width: 30px; height: 30px; background: #fff;
  }
  .back-web {
    position: absolute; left: 0; right: 0; bottom: 48px;
    text-align: center; color: #fff; font-size: 13px; letter-spacing: 1px;
  }

  /* Front side */
  .card-front { left: 500px; top: 466px; background: var(--card-white); }
  .front-brand {
    position: absolute; right: 34px; top: 118px;
    display: flex; align-items: center; gap: 12px;
    color: var(--ink); font-weight: 700; font-size: 44px; letter-spacing: -1px;
  }
  .front-brand .brand-square {
    width: 28px; height: 28px; background: var(--blue);
  }
  .front-bands { position: absolute; left: 0; top: 0; }
  .front-web {
    position: absolute; right: 28px; top: 268px;
    color: #fff; font-size: 13px; letter-spacing: .5px;
  }

  .contact { position: absolute; left: 32px; top: 134px; }
  .contact-name { color: var(--blue); font-weight: 700; font-size: 20px; line-height: 1.1; }
  .contact-title { color: var(--ink-soft); font-size: 13px; margin-bottom: 14px; }
  .contact-list { list-style: none; }
  .contact-list li {
    display: flex; align-items: center; gap: 10px;
    color: var(--ink); font-size: 13px; line-height: 21px;
  }
  .contact-list svg { width: 14px; height: 14px; flex: none; }
</style>
</head>
<body>
<main class="canvas">

  <section class="card card-back" aria-label="Business card back">
    <div class="back-brand"><span class="brand-square"></span>RM Cargoline</div>
    <div class="back-web">www.rmcargoline.example</div>
  </section>

  <section class="card card-front" aria-label="Business card front">
    <svg class="front-bands" width="620" height="354" viewBox="0 0 620 354" aria-hidden="true">
      <polygon points="372,258 620,258 620,298 350,298" fill="var(--blue)"/>
      <polygon points="350,298 620,298 620,316 340,316" fill="var(--band-dark)"/>
      <polygon points="0,316 340,316 350,298 356,298 344,322 0,322" fill="var(--blue-dark)"/>
      <rect x="0" y="322" width="620" height="32" fill="var(--band-dark)"/>
    </svg>

    <div class="front-brand"><span class="brand-square"></span>RM Cargoline</div>
    <div class="front-web">www.rmcargoline.example</div>

    <div class="contact">
      <div class="contact-name">Berki Zsófia</div>
      <div class="contact-title">General Manager</div>
      <ul class="contact-list">
        <li>
          <svg viewBox="0 0 14 14"><rect x="3.5" y="1" width="7" height="12" rx="1.2" fill="none" stroke="var(--blue)" stroke-width="1.3"/><circle cx="7" cy="11" r=".7" fill="var(--blue)"/></svg>
          +36-70/482-5193
        </li>
        <li>
          <svg viewBox="0 0 14 14"><rect x="4" y="1.5" width="6" height="3.5" fill="var(--blue)"/><rect x="1.5" y="5" width="11" height="5" rx="1" fill="var(--blue)"/><rect x="4" y="9" width="6" height="3.5" fill="#fff" stroke="var(--blue)" stroke-width="1"/></svg>
          +36-1/534-9061
        </li>
        <li>
          <svg viewBox="0 0 14 14"><rect x="1" y="3" width="12" height="8.5" fill="none" stroke="var(--blue)" stroke-width="1.2"/><polyline points="1,3 7,8 13,3" fill="none" stroke="var(--blue)" stroke-width="1.2"/></svg>
          zsofia.berki@rmcargoline.example
        </li>
        <li>
          <svg viewBox="0 0 14 14"><rect x="1" y="3" width="12" height="8.5" fill="none" stroke="var(--blue)" stroke-width="1.2"/><polyline points="1,3 7,8 13,3" fill="none" stroke="var(--blue)" stroke-width="1.2"/></svg>
          info@rmcargoline.example
        </li>
      </ul>
    </div>
  </section>

</main>
</body>
</html>
```